Larkfold Inn Weekly Special Flyer

Looking for a professional weekly special promotion flyer to handout. Something I can edit and use as specials change. We are a small bar in a rural town (country). Something that can be use everyday software

Larkfold Inn
418 West Cedar Avenue
Wellington, Ohio 44987
(440) 555-0193
Join Us on Chatterbook \Larkfoldinn

$1.00 Domestic Drafts every day during happy hour
Happy hour hours = Mon-Fri 3-7 Sat & Sun 12-7

Sundays:
Free Pool ALL day on both tables
$1.00 Domestic drafts until midnight

$3.00 Appetizers
$4.00 Glacine Bloody Marys
$5.00 3 - topping pizza

Mondays:
$2.00 Well Margaritas
$3.00 5 Pebble Vodka Bombs
$4.00 Rum Runners
$6.00 Philly Cheese Steak Sandwich served with loaded fries

Tuesdays:
$2.00 Harvest Radler
$3.00 Gray Heron
$3.00 Loaded Nachos
$3.00 Loaded Fries
$4.00 Liquid Marijuana's

Wednesdays:
$2.00 Quiet Meadow Bottles
$3.00 Blue Stars
$3.00 Fizzle Twigs
$4.00 Bartender Bombs
$4.00 2 Topping Pizzas

Thursdays:
~*~*Ladies Night Thursday*~
$3.00 Tart Crumb
$3.00 Sweet Affair
$3 1/2 dozen wings!
$4.00 Spin Doctors
LADIES ONLY SPECIALS
$2.00 5 Pebble Shots
$3.00 Long Islands
$4.00 Bartender Bombs!

Fridays:
$2.00 Mele Nalu Pineapple Beer
$2.00 Lumbermans brew
$2.00 Knotted Cup
$2.00 Restless Rover
$3.00 Little Beers
$3.00 banana pepper rings...
$3.00 hot pepper cheese balls
$4.00 Washington Apples

Saturdays:
Extended Happy Hour (12-8)
$1.00 Domestic Drafts
$2.00 Wine Coolers
$2.00 Lumbermans Brew
$2.00 Pellows Hard Iced Tea
$3.00 Sweet Affair
$3.00 Irish Breakfast Shots
$4.00 Irish Car Bombs
$4.00 Orbit Lollies
~*Until 8PM*~

add some tear off coupons that I can edit dollars and offers:
$2.00 off Pizza
$2.00 Philly Cheese Steak
Contact for us for birthday party discounts and fund raising events

attached is our company logo

I also attached a flyer of something I liked I picked up

```html
<!DOCTYPE html>
<html lang="en">
<head>
<meta charset="utf-8">
<title>Larkfold Inn Weekly Specials</title>
<link rel="stylesheet" href="https://fonts.googleapis.com/css2?family=Libre+Baskerville:wght@400;700&family=Oswald:wght@400;500&family=Patrick+Hand&display=swap">
<style>
:root{
  --red-deep:#a3130f;
  --red:#d11f16;
  --price-red:#e0261a;
  --pink:#e8227a;
  --yellow:#ffd21a;
  --orange:#f39a12;
  --cream:#fff6d6;
  --cream-edge:#f4dfa0;
  --ink:#141010;
  --footer:#151312;
  --white:#ffffff;
}
*{margin:0;padding:0;box-sizing:border-box}
html,body{width:927px;height:1200px;overflow:hidden}
body{font-family:"Libre Baskerville",Georgia,serif;color:var(--ink)}
.flyer{position:relative;width:927px;height:1200px;overflow:hidden;
  background:
    radial-gradient(ellipse 520px 420px at 60px 120px,var(--yellow) 0%,var(--orange) 35%,rgba(209,31,22,0) 75%),
    radial-gradient(ellipse 420px 300px at 900px 1060px,var(--yellow) 0%,rgba(243,154,18,.6) 35%,rgba(209,31,22,0) 75%),
    linear-gradient(160deg,var(--red) 0%,var(--red-deep) 100%);}

.brand{position:absolute;left:40px;top:80px;width:270px;height:160px;display:flex;align-items:center;gap:12px}
.brand-dot{width:30px;height:30px;border-radius:50%;background:var(--red-deep);flex:none}
.brand-name{font-weight:700;font-size:36px;line-height:1.1;color:var(--red-deep)}

.panel{position:absolute;background:radial-gradient(ellipse at center,var(--cream) 55%,var(--cream-edge) 100%);
  border-radius:4px;box-shadow:0 2px 6px rgba(60,0,0,.45);padding:14px 12px 10px 14px}
.panel h2{font-weight:700;font-size:24px;letter-spacing:-.6px;line-height:1;margin-bottom:8px;white-space:nowrap}
.specials{list-style:none;position:relative;z-index:1}
.specials li{display:grid;grid-template-columns:72px 1fr;align-items:start;font-size:14.5px;line-height:1.2;margin-bottom:6px}
.price{color:var(--price-red);font-weight:700;font-size:17.5px;line-height:1.05}
.tight li{margin-bottom:2px;font-size:14px;line-height:1.15}
.tag{color:var(--price-red);font-weight:700;font-size:17px;line-height:1.15;margin:2px 0 3px}
.tag.pink{color:var(--pink)}
.photo{position:absolute;border-radius:8px}

/* Sunday */
.sunday{left:332px;top:43px;width:554px;height:215px}
.sunday h2{font-size:29px}
.free-pool{position:absolute;left:20px;top:60px;width:105px;height:130px;border:4px solid #5a1016;background:var(--cream);padding:8px 6px;font-size:13.5px;line-height:1.2;text-transform:uppercase}
.free-pool strong{display:block;color:var(--price-red);font-size:20px;margin-bottom:2px}
.sunday .photo{left:132px;top:70px;width:80px;height:128px;background:radial-gradient(ellipse at 45% 40%,#c4141a 0%,#8a1010 35%,rgba(230,190,110,.8) 62%,rgba(255,246,214,0) 78%)}
.sunday-list{position:absolute;right:16px;top:52px;list-style:none;text-align:right}
.sunday-list li{font-size:15.5px;margin-bottom:8px;white-space:nowrap}
.sunday-list li:nth-child(1){margin-right:70px}
.sunday-list li:nth-child(2){margin-right:190px}
.sunday-list li:nth-child(3){margin-right:28px}
.sunday-list .price{font-size:21px;margin-right:6px}

/* rows */
.monday{left:46px;top:273px;width:268px;height:335px}
.tuesday{left:335px;top:273px;width:260px;height:335px}
.wednesday{left:616px;top:273px;width:268px;height:335px}
.thursday{left:46px;top:630px;width:268px;height:333px}
.friday{left:335px;top:630px;width:260px;height:333px}
.saturday{left:616px;top:630px;width:268px;height:333px}

.monday .photo{left:30px;bottom:20px;width:210px;height:92px;background:linear-gradient(180deg,#d8a25c,#8c5a2e 55%,#e7c98a)}
.tuesday .photo{left:10px;bottom:12px;width:240px;height:110px;background:radial-gradient(ellipse at center,#f0b23a 0%,#d98a22 50%,rgba(255,246,214,0) 78%)}
.wednesday .photo.bottle{left:20px;bottom:22px;width:36px;height:120px;background:linear-gradient(180deg,#2a4a20,#5a3a14)}
.wednesday .photo.pie{left:72px;bottom:18px;width:168px;height:120px;border-radius:50%;background:radial-gradient(circle,#c2451e 0%,#d9822e 70%,#b86a22 100%)}

.thursday .narrow li{padding-right:66px}
.thursday .photo{right:8px;bottom:14px;width:58px;height:118px;background:linear-gradient(180deg,rgba(230,40,120,.85),rgba(30,20,20,.9))}

.friday .beside{padding-right:58px}
.friday .photo.bottles{left:12px;bottom:10px;width:58px;height:42px;background:linear-gradient(180deg,#6a1e12,#2a0a06)}
.friday .photo.can{right:10px;bottom:14px;width:48px;height:88px;background:linear-gradient(90deg,#d8d088,#f4f0c8,#c2b860)}

.saturday .tight li{font-size:13.5px}
.until{color:var(--price-red);font-weight:700;font-size:16px;margin-top:4px}

/* bottom band */
.daily{position:absolute;left:44px;top:978px;color:var(--yellow);display:flex;align-items:center;gap:6px}
.daily .big{font-size:29px;font-weight:700}
.daily .small{font-family:"Oswald",sans-serif;font-size:16px;line-height:1;text-transform:uppercase;letter-spacing:.5px}
.happy{position:absolute;left:44px;top:1026px;font-family:"Oswald",sans-serif;color:var(--yellow);font-size:44px;line-height:1;font-weight:500}
.hours{position:absolute;left:214px;top:1036px;font-family:"Oswald",sans-serif;color:var(--yellow);font-size:22px;line-height:1.1}
.coupon{position:absolute;top:987px;width:140px;height:129px;background:var(--white);border:1px solid #999;padding:10px 8px}
.coupon.pizza{left:405px}
.coupon.steak{left:552px}
.coupon .amt{color:var(--price-red);font-weight:700;font-size:28px;display:inline-block}
.coupon .off{display:inline-block;writing-mode:vertical-rl;font-size:9px;font-weight:700;color:var(--price-red);vertical-align:top;margin-left:2px}
.coupon .item{font-weight:700;font-size:21px;line-height:1.05;margin-top:6px;text-transform:uppercase}
.coupon.pizza .item{font-size:25px}
.contact{position:absolute;left:712px;top:986px;width:180px;font-family:"Patrick Hand",sans-serif;font-size:16px;line-height:1.12;color:var(--ink);text-transform:uppercase}
.balloons{position:absolute;left:730px;top:1062px;width:190px;height:64px;border-radius:40px 40px 0 0;background:radial-gradient(ellipse at 50% 80%,#e02020 0%,#f06a6a 40%,rgba(255,210,40,0) 75%)}

/* footer */
.footer{position:absolute;left:0;top:1128px;width:927px;height:72px;background:var(--footer);display:flex;align-items:center;padding-left:44px;color:var(--white);white-space:nowrap}
.footer .name{color:var(--yellow);font-weight:700;font-size:25px;padding-right:12px;border-right:1px solid #888}
.footer .addr{font-size:12.5px;line-height:1.35;padding:0 12px;border-right:1px solid #888}
.footer .phone{color:var(--yellow);font-weight:700;font-size:19px;padding:0 12px;border-right:1px solid #888}
.footer .social{font-size:13.5px;padding-left:12px}
.footer .social span{color:var(--yellow)}
</style>
</head>
<body>
<main class="flyer">

  <div class="brand">
    <span class="brand-dot"></span>
    <span class="brand-name">LARKFOLD INN</span>
  </div>

  <section class="panel sunday">
    <h2>SUNDAYS:</h2>
    <div class="free-pool"><strong>Free</strong>Pool all day on both tables</div>
    <div class="photo" role="img" aria-label="Bloody Mary cocktail and a pizza"></div>
    <ul class="sunday-list">
      <li><span class="price">$1.00</span>Domestic drafts until midnight</li>
      <li><span class="price">$3.00</span>Appetizers</li>
      <li><span class="price">$4.00</span>Glacine Bloody Marys</li>
      <li><span class="price">$5.00</span>3 - topping pizza</li>
    </ul>
  </section>

  <section class="panel monday">
    <h2>MONDAYS:</h2>
    <ul class="specials">
      <li><span class="price">$2.00</span>Well Margaritas</li>
      <li><span class="price">$3.00</span>5 Pebble Vodka Bombs</li>
      <li><span class="price">$4.00</span>Rum Runners</li>
      <li><span class="price">$6.00</span>Philly Cheese Steak Sandwich served with loaded fries</li>
    </ul>
    <div class="photo" role="img" aria-label="Philly cheese steak sandwich"></div>
  </section>

  <section class="panel tuesday">
    <h2>TUESDAYS:</h2>
    <ul class="specials">
      <li><span class="price">$2.00</span>Harvest Radler</li>
      <li><span class="price">$3.00</span>Gray Heron</li>
      <li><span class="price">$3.00</span>Loaded Nachos</li>
      <li><span class="price">$3.00</span>Loaded Fries</li>
      <li><span class="price">$4.00</span>Liquid Marijuana’s</li>
    </ul>
    <div class="photo" role="img" aria-label="Plate of loaded fries"></div>
  </section>

  <section class="panel wednesday">
    <h2>WEDNESDAYS:</h2>
    <ul class="specials">
      <li><span class="price">$2.00</span>Quiet Meadow Bottles</li>
      <li><span class="price">$3.00</span>Blue Stars</li>
      <li><span class="price">$3.00</span>Fizzle Twigs</li>
      <li><span class="price">$4.00</span>Bartender Bombs</li>
      <li><span class="price">$4.00</span>2 Topping Pizzas</li>
    </ul>
    <div class="photo bottle" role="img" aria-label="Bottle of cider"></div>
    <div class="photo pie" role="img" aria-label="Two topping pizza"></div>
  </section>

  <section class="panel thursday">
    <h2>THURSDAYS:</h2>
    <p class="tag pink">LADIES NIGHT</p>
    <ul class="specials tight">
      <li><span class="price">$3.00</span>Tart Crumb</li>
      <li><span class="price">$3.00</span>Sweet Affair</li>
      <li><span class="price">$3.00</span>1/2 Dozen Wings!</li>
      <li><span class="price">$4.00</span>Spin Doctors</li>
    </ul>
    <p class="tag pink">LADIES ONLY<br>SPECIALS</p>
    <ul class="specials tight narrow">
      <li><span class="price">$2.00</span>5 Pebble Shots</li>
      <li><span class="price">$3.00</span>Long Islands</li>
      <li><span class="price">$4.00</span>Bartender Bombs!</li>
    </ul>
    <div class="photo" role="img" aria-label="Pink cocktail glass and high heel shoe"></div>
  </section>

  <section class="panel friday">
    <h2>FRIDAYS:</h2>
    <ul class="specials tight">
      <li><span class="price">$2.00</span>Mele Nalu Pineapple Beer</li>
      <li><span class="price">$2.00</span>Lumbermans Brew</li>
      <li><span class="price">$2.00</span>Knotted Cup</li>
      <li><span class="price">$2.00</span>Restless Rover</li>
      <li><span class="price">$3.00</span>Little Beers</li>
      <li><span class="price">$3.00</span>Banana Pepper Rings...</li>
      <li class="beside"><span class="price">$3.00</span>Hot Pepper Cheese Balls</li>
      <li class="beside"><span class="price">$4.00</span>Washington Apples</li>
    </ul>
    <div class="photo bottles" role="img" aria-label="Three small beer bottles"></div>
    <div class="photo can" role="img" aria-label="Pineapple beer can"></div>
  </section>

  <section class="panel saturday">
    <h2>SATURDAYS:</h2>
    <p class="tag">EXTENDED<br>HAPPY HOUR (12-8)</p>
    <ul class="specials tight">
      <li><span class="price">$1.00</span>Domestic Drafts</li>
      <li><span class="price">$2.00</span>Wine Coolers</li>
      <li><span class="price">$2.00</span>Lumbermans Brew</li>
      <li><span class="price">$2.00</span>Pellows Hard Iced Tea</li>
      <li><span class="price">$3.00</span>Banana Pepper Rings...</li>
      <li><span class="price">$3.00</span>Sweet Affair</li>
      <li><span class="price">$4.00</span>Irish Breakfast Shots</li>
      <li><span class="price">$4.00</span>Irish Car Bombs</li>
      <li><span class="price">$4.00</span>Orbit Lollies</li>
    </ul>
    <p class="until">UNTIL 8PM</p>
  </section>

  <div class="daily"><span class="big">$1.00</span><span class="small">Domestic Drafts Every Day<br>During Happy Hour</span></div>
  <div class="happy">HAPPY<br>HOUR</div>
  <div class="hours">HOURS<br>MON-FRI 3-7<br>SAT &amp; SUN 12-7</div>

  <div class="coupon pizza"><span class="amt">$2.00</span><span class="off">OFF</span><p class="item">Pizza</p></div>
  <div class="coupon steak"><span class="amt">$2.00</span><span class="off">OFF</span><p class="item">Philly Cheese Steak</p></div>

  <p class="contact">Contact for us for birthday party discounts and fund raising events</p>
  <div class="balloons" role="img" aria-label="Party balloons"></div>

  <footer class="footer">
    <span class="name">LARKFOLD INN</span>
    <span class="addr">418 West Cedar Avenue<br>Wellington, Ohio 44987</span>
    <span class="phone">(440) 555-0193</span>
    <span class="social">Join Us on <span>Chatterbook \Larkfoldinn</span></span>
  </footer>

</main>
</body>
</html>
```